Poster & Banner for Outback tour company

Poster needed for tour company in the Australian outback. We will need it in an A2 format and if possible a larger banner format as Well please. It needs the Kestrel Tours logo but also the other logos (less obvious). It also needs to feature the Vantorix logo (uploaded).

The poster needs a list of the tours we offer as well as some of the pictures uploaded.

List of tours:

- Deluxe Tour of the Village and the Redspurs $99
- Marrandi Scenic Tour $85
- Starlight Redspurs Tour $60
- Quartz Trailside Tour $50

Industry/Entity Type

Tour Company

Font styles to use
Serif

Colors

Designer to choose colors to be used in the design.

Requirements
Must have
• Kestrel Tours logo/List of tours/

```html
<!DOCTYPE html>
<html lang="en">
<head>
<meta charset="utf-8">
<title>Kestrel Tours – Outback Tours Poster</title>
<link rel="stylesheet" href="https://fonts.googleapis.com/css2?family=Oswald:wght@500;600&family=Permanent+Marker&display=swap">
<style>
  :root {
    --bg: #eceeee;
    --sky-top: #7f9fd4;
    --sky-low: #a8bedc;
    --rock: #c27548;
    --rock-deep: #9a4e2e;
    --red: #b0222a;
    --orange: #f4961e;
    --ink: #2a1a14;
    --white: #ffffff;
    --brand: #3a2a22;
    --badge: #5cc38a;
    --divider: #333333;
  }
  * { margin: 0; padding: 0; box-sizing: border-box; }
  html, body { width: 1200px; height: 1200px; overflow: hidden; background: var(--bg); }
  .poster {
    position: absolute; left: 211px; top: 50px;
    width: 778px; height: 1100px;
    background: var(--white);
    overflow: hidden;
  }
  .hero-photo {
    position: absolute; left: 0; top: 0; width: 778px; height: 965px;
    background: linear-gradient(180deg, var(--sky-top) 0%, var(--sky-low) 45%, var(--rock) 75%, var(--rock-deep) 100%);
  }
  .torn-edge { position: absolute; left: 0; top: 952px; width: 778px; height: 20px; }
  .brand {
    position: absolute; left: 476px; top: 104px;
    display: flex; align-items: center; gap: 10px;
    font-family: "Oswald", sans-serif; font-weight: 600;
    font-size: 30px; letter-spacing: 1px; color: var(--brand);
  }
  .brand-square { width: 22px; height: 22px; background: var(--red); }
  .tour {
    position: absolute;
    display: flex; align-items: center; justify-content: space-between;
  }
  .tour svg.stroke { position: absolute; inset: 0; width: 100%; height: 100%; }
  .tour-name {
    position: relative; white-space: nowrap;
    font-family: "Permanent Marker", "Oswald", sans-serif;
    font-size: 24px; line-height: 1.2;
  }
  .tour-price {
    position: relative; white-space: nowrap;
    font-family: "Permanent Marker", "Oswald", sans-serif;
    font-size: 80px; line-height: 1;
  }
  .tour--red .tour-name, .tour--red .tour-price { color: var(--white); }
  .tour--orange .tour-name, .tour--orange .tour-price { color: var(--ink); }
  .tour-starlight { left: 236px; top: 246px; width: 430px; height: 84px; padding: 0 34px 0 40px; }
  .tour-deluxe { left: 206px; top: 338px; width: 518px; height: 88px; padding: 0 22px 0 22px; }
  .tour-deluxe .tour-name { font-size: 22px; }
  .tour-quartz { left: 262px; top: 437px; width: 414px; height: 96px; padding: 0 42px 0 46px; }
  .tour-marrandi { left: 246px; top: 552px; width: 414px; height: 78px; padding: 0 36px 0 54px; }
  .website {
    position: absolute; left: 0; width: 778px; top: 868px; text-align: center;
    font-family: "Oswald", sans-serif; font-weight: 500;
    font-size: 30px; color: var(--white); letter-spacing: 0.5px;
  }
  .partners {
    position: absolute; left: 0; top: 985px; width: 778px; height: 115px;
    display: flex; align-items: center; justify-content: center; gap: 24px;
    font-family: "Oswald", sans-serif; font-weight: 500;
  }
  .partner { font-size: 20px; line-height: 1.05; text-align: center; }
  .partner--motel { color: #c8612a; }
  .partner--resort { color: #b83a1e; font-size: 15px; }
  .partner--parks { color: #2f5fa8; }
  .partner--villages { color: #6cae3c; }
  .partner-divider { width: 2px; height: 70px; background: var(--divider); }
  .award { display: flex; align-items: center; gap: 8px; }
  .award-badge { width: 40px; height: 46px; background: var(--badge); }
  .award-name { font-size: 18px; color: #2e8a5a; }
</style>
</head>
<body>
  <main class="poster">
    <div class="hero-photo" role="img" aria-label="Photo placeholder: tour truck parked beneath a sandstone cave arch in the outback, with eroded mesas and blue sky behind"></div>
    <svg class="torn-edge" viewBox="0 0 778 20" preserveAspectRatio="none" aria-hidden="true">
      <polygon fill="#ffffff" points="0,14 40,8 80,13 130,6 180,12 230,7 290,13 340,8 400,12 450,5 510,12 560,8 620,13 670,7 730,12 778,8 778,20 0,20"/>
    </svg>

    <div class="brand"><span class="brand-square"></span>KESTREL TOURS</div>

    <section class="tour-list">
      <div class="tour tour--red tour-starlight">
        <svg class="stroke" viewBox="0 0 100 100" preserveAspectRatio="none" aria-hidden="true"><polygon fill="#b0222a" points="3,4 30,0 60,5 95,2 100,96 70,100 35,95 0,98 2,50"/></svg>
        <span class="tour-name">STARLIGHT<br>REDSPURS TOUR</span>
        <span class="tour-price">$60</span>
      </div>
      <div class="tour tour--orange tour-deluxe">
        <svg class="stroke" viewBox="0 0 100 100" preserveAspectRatio="none" aria-hidden="true"><polygon fill="#f4961e" points="0,6 35,2 70,6 96,0 100,92 60,100 25,95 1,98"/></svg>
        <span class="tour-name">DELUXE TOUR OF THE<br>VILLAGE AND THE REDSPURS</span>
        <span class="tour-price">$99</span>
      </div>
      <div class="tour tour--red tour-quartz">
        <svg class="stroke" viewBox="0 0 100 100" preserveAspectRatio="none" aria-hidden="true"><polygon fill="#b0222a" points="6,6 40,2 75,5 100,0 97,95 55,100 20,96 0,90"/></svg>
        <span class="tour-name">QUARTZ<br>TRAILSIDE TOUR</span>
        <span class="tour-price">$50</span>
      </div>
      <div class="tour tour--orange tour-marrandi">
        <svg class="stroke" viewBox="0 0 100 100" preserveAspectRatio="none" aria-hidden="true"><polygon fill="#f4961e" points="3,8 40,3 70,6 98,0 100,94 60,98 30,96 0,100"/></svg>
        <span class="tour-name">MARRANDI<br>SCENIC TOUR</span>
        <span class="tour-price">$85</span>
      </div>
    </section>

    <p class="website">KESTRELTOURSAUSTRALIA.COM.AU</p>

    <footer class="partners">
      <span class="partner partner--motel">CLAYPAN<br>MOTEL</span>
      <span class="partner partner--resort">RIDGEWAY<br>OUTBACK RESORT</span>
      <span class="partner-divider"></span>
      <span class="partner partner--parks">PARKLINE<br>HOLIDAY PARKS</span>
      <span class="partner-divider"></span>
      <span class="partner partner--villages">WILLOWBANK<br>VILLAGES</span>
      <span class="award">
        <span class="award-badge" role="img" aria-label="Vantorix travellers' award badge"></span>
        <span class="award-name">VANTORIX</span>
      </span>
    </footer>
  </main>
</body>
</html>
```